Flyer für Sicherheitsfirma
Zielgruppe
Wir sind eine Sicherheitsfirma und verkaufen und installieren Alarmanlagen, Kamerasysteme und Brandmeldeanlagen.
Aufgabenstellung
Es sollte ein sehr ansprechender Flyer sein, welcher in dem Bewohner des Hauses die Angst weckt das ihm Einbruch oder Brand auch jederzeit widerfahren kann.

```html
<!DOCTYPE html>
<html lang="de">
<head>
<meta charset="utf-8">
<title>WACHTPUNKT – Flyer</title>
<link rel="stylesheet" href="https://fonts.googleapis.com/css2?family=Anton&family=Poppins:wght@400;500;600;700;800&display=swap">
<style>
  :root {
    --red: #e31e24;
    --red-dark: #8f0f14;
    --black: #0d0d0d;
    --white: #ffffff;
    --ink: #1c1c1c;
    --stage: #a8a8a8;
    --brand-grey: #4a4f53;
  }
  * { box-sizing: border-box; margin: 0; padding: 0; }
  html, body { width: 1200px; height: 1117px; overflow: hidden; }
  body { background: var(--stage); font-family: 'Poppins', sans-serif; position: relative; }

  .flyer { position: absolute; top: 215px; width: 535px; height: 756px; overflow: hidden; background: var(--white); }
  .flyer--front { left: 56px; }
  .flyer--back { left: 609px; }
  .abs { position: absolute; }

  /* company name */
  .brand { display: flex; align-items: center; gap: 8px; }
  .brand__dot { width: 18px; height: 18px; border-radius: 50%; background: var(--red); flex: none; }
  .brand__name { font-family: 'Poppins', sans-serif; font-weight: 600; color: var(--brand-grey); font-size: 20px; letter-spacing: .5px; line-height: 1; }

  /* front */
  .front__hero { left: 0; top: 0; width: 535px; height: 412px; background: radial-gradient(ellipse at 70% 60%, #c7261c 0%, #9c1216 45%, #6d0b0e 100%); }
  .front__plate { left: 0; top: 0; width: 535px; height: 74px; }
  .front__logo { left: 148px; top: 0; width: 239px; height: 72px; display: flex; justify-content: center; align-items: center; }
  .front__headline { left: 0; top: 84px; width: 535px; text-align: center; font-family: 'Anton', sans-serif; font-weight: 400; color: var(--white); font-size: 46px; line-height: 49px; letter-spacing: .2px; }
  .front__subline { left: 0; top: 187px; width: 535px; text-align: center; color: var(--white); font-weight: 600; font-size: 16.5px; }
  .front__subline .sep { color: var(--red); }
  .front__strip { left: 37px; top: 218px; width: 464px; height: 104px; }
  .front__tab { left: 56px; top: 303px; width: 240px; height: 36px; }
  .front__tab-text { left: 74px; top: 309px; color: var(--white); font-weight: 700; font-size: 16px; }
  .front__band { left: 56px; top: 320px; width: 479px; height: 91px; background: var(--black); }
  .front__band-text { left: 88px; top: 344px; width: 424px; color: var(--white); font-weight: 600; font-size: 13.4px; line-height: 17.5px; }
  .front__photo { left: 0; top: 411px; width: 535px; height: 294px; }
  .front__intro { left: 296px; top: 424px; font-weight: 700; font-size: 15px; line-height: 18px; color: var(--ink); }
  .solution { position: absolute; }
  .solution__title { color: var(--red); font-weight: 700; font-size: 15.5px; line-height: 19px; }
  .solution__text { color: var(--ink); font-size: 15px; line-height: 19px; }
  .front__rule { position: absolute; height: 1.5px; background: var(--red); }
  .front__cta { left: 0; top: 705px; width: 535px; height: 51px; background: var(--red); color: var(--white); font-weight: 700; font-size: 13px; display: flex; align-items: center; justify-content: center; }

  /* back */
  .back__photo { left: 0; top: 0; width: 535px; height: 176px; }
  .back__red-lower { left: 0; top: 392px; width: 535px; height: 265px; background: linear-gradient(120deg, #a51418, #6e0b0e); }
  .back__dark-strip { left: 0; top: 176px; width: 24px; height: 240px; background: var(--black); }
  .back__panel { left: 23px; top: 175px; width: 489px; height: 281px; background: var(--white); }
  .back__tab { left: 0; top: 164px; width: 330px; height: 36px; }
  .back__tab-text { left: 54px; top: 170px; color: var(--white); font-weight: 700; font-size: 17px; }
  .back__logo { left: 370px; top: 190px; }
  .benefit__icon { position: absolute; left: 46px; }
  .benefit__title { position: absolute; left: 131px; font-weight: 700; font-size: 15.5px; color: var(--ink); }
  .benefit__text { position: absolute; left: 131px; width: 345px; font-size: 12.2px; line-height: 15px; color: #2a2a2a; }
  .back__rule { position: absolute; left: 131px; width: 356px; height: 1.5px; background: var(--red); }
  .back__portrait { left: 0; top: 456px; width: 300px; height: 201px; }
  .back__why { left: 289px; top: 476px; color: var(--white); font-weight: 700; font-size: 20px; line-height: 23px; }
  .back__why-rule { left: 289px; top: 532px; width: 198px; height: 1.5px; background: var(--white); }
  .back__list { left: 293px; top: 548px; width: 200px; list-style: none; color: var(--white); font-weight: 700; font-size: 10.8px; line-height: 15.5px; }
  .back__list li { display: flex; gap: 7px; margin-bottom: 9px; }
  .back__list li span { max-width: 170px; }
  .back__list svg { flex: none; margin-top: 2px; }
  .back__footer { left: 0; top: 657px; width: 535px; height: 99px; background: var(--red); color: var(--white); }
  .contact__role { left: 46px; top: 13px; font-weight: 500; font-size: 11.5px; }
  .contact__name { left: 46px; top: 23px; font-weight: 700; font-size: 28px; }
  .contact__line { left: 46px; top: 62px; font-weight: 600; font-size: 11.5px; display: flex; gap: 10px; align-items: center; white-space: nowrap; }
  .contact__line span { display: inline-flex; gap: 4px; align-items: center; }
  .contact__divider { left: 332px; top: 14px; width: 1.5px; height: 66px; background: rgba(255,255,255,.6); }
  .contact__address { left: 346px; top: 25px; font-weight: 700; font-size: 12px; line-height: 17px; display: flex; gap: 5px; }
</style>
</head>
<body>

<section class="flyer flyer--front">
  <div class="abs front__hero" role="img" aria-label="Hintergrundbild: Einbrecher und Flammen in dunklem Rot"></div>

  <svg class="abs front__plate" viewBox="0 0 535 74">
    <polygon points="148,0 387,0 366,72 170,72" fill="#fff"/>
  </svg>
  <div class="abs front__logo">
    <div class="brand"><span class="brand__dot"></span><span class="brand__name">WACHTPUNKT</span></div>
  </div>

  <h1 class="abs front__headline">SCHÜTZEN SIE, WAS IHNEN<br>AM WICHTIGSTEN IST!</h1>
  <p class="abs front__subline">Ihr Zuhause <span class="sep">•</span> Ihre Familie <span class="sep">•</span> Ihre Sicherheit.</p>

  <svg class="abs front__strip" viewBox="0 0 464 104">
    <defs>
      <linearGradient id="gSmoke" x1="0" x2="1"><stop offset="0" stop-color="#f2f2f2"/><stop offset="1" stop-color="#bdbdbd"/></linearGradient>
      <linearGradient id="gFire" x1="0" x2="1"><stop offset="0" stop-color="#5a3a20"/><stop offset="1" stop-color="#e88a2a"/></linearGradient>
      <linearGradient id="gNight" x1="0" x2="1"><stop offset="0" stop-color="#3a5878"/><stop offset="1" stop-color="#1b2b3d"/></linearGradient>
    </defs>
    <polygon points="18,0 464,0 446,104 0,104" fill="#fff"/>
    <polygon points="24,4 164,4 148,100 7,100" fill="url(#gSmoke)" role="img" aria-label="Foto: Rauchmelder an der Decke"/>
    <polygon points="166,4 305,4 290,100 150,100" fill="url(#gFire)" role="img" aria-label="Foto: Person flieht vor Feuer zum Notausgang"/>
    <polygon points="307,4 458,4 441,100 292,100" fill="url(#gNight)" role="img" aria-label="Foto: Einbrecher mit Brecheisen am Fenster"/>
  </svg>

  <div class="abs front__band"></div>
  <svg class="abs front__tab" viewBox="0 0 240 36"><polygon points="6,0 240,0 234,36 0,36" fill="#e31e24"/></svg>
  <div class="abs front__tab-text">Sind Sie wirklich sicher?</div>
  <p class="abs front__band-text">Einbrüche, Vandalismus und Brände können unerwartet passieren. Schützen Sie Ihr Zuhause und gewinnen Sie ein gutes Gefühl von Sicherheit zurück.</p>

  <svg class="abs front__photo" viewBox="0 0 535 294">
    <defs><linearGradient id="gBurglar" x1="0" x2="1" y1="0" y2="1"><stop offset="0" stop-color="#3b4a5c"/><stop offset="1" stop-color="#101419"/></linearGradient></defs>
    <rect x="0" y="0" width="300" height="294" fill="url(#gBurglar)" role="img" aria-label="Foto: maskierter Einbrecher mit Taschenlampe"/>
    <polygon points="277,0 535,0 535,294 220,294" fill="#fff"/>
  </svg>

  <p class="abs front__intro">Entdecken Sie<br>modernste Lösungen für:</p>
  <div class="front__rule" style="left:292px;top:472px;width:206px"></div>

  <svg class="abs" style="left:238px;top:489px" width="42" height="42" viewBox="0 0 42 42"><circle cx="21" cy="21" r="20" fill="#fff" stroke="#e31e24" stroke-width="2"/><circle cx="21" cy="21" r="12" fill="#e31e24"/><path d="M15 21l4 4 8-8" fill="none" stroke="#fff" stroke-width="3" stroke-linecap="round" stroke-linejoin="round"/></svg>
  <div class="solution" style="left:294px;top:485px"><div class="solution__title">Alarmanlagen</div><div class="solution__text">Effektiver Schutz vor<br>Einbrüchen.</div></div>
  <div class="front__rule" style="left:287px;top:553px;width:211px"></div>

  <svg class="abs" style="left:223px;top:556px" width="42" height="42" viewBox="0 0 42 42"><circle cx="21" cy="21" r="20" fill="#fff" stroke="#e31e24" stroke-width="2"/><circle cx="21" cy="21" r="12" fill="#e31e24"/><path d="M15 21l4 4 8-8" fill="none" stroke="#fff" stroke-width="3" stroke-linecap="round" stroke-linejoin="round"/></svg>
  <div class="solution" style="left:286px;top:563px"><div class="solution__title">Kamerasysteme</div><div class="solution__text">Alles im Blick, jederzeit.</div></div>
  <div class="front__rule" style="left:272px;top:614px;width:226px"></div>

  <svg class="abs" style="left:209px;top:625px" width="42" height="42" viewBox="0 0 42 42"><circle cx="21" cy="21" r="20" fill="#fff" stroke="#e31e24" stroke-width="2"/><circle cx="21" cy="21" r="12" fill="#e31e24"/><path d="M15 21l4 4 8-8" fill="none" stroke="#fff" stroke-width="3" stroke-linecap="round" stroke-linejoin="round"/></svg>
  <div class="solution" style="left:272px;top:625px"><div class="solution__title">Brandmeldeanlagen</div><div class="solution__text">Frühzeitige Warnung rettet<br>Leben.</div></div>

  <div class="abs front__cta">Jetzt einen unverbindlichen Beratungstermin vor Ort vereinbaren!</div>
</section>

<section class="flyer flyer--back">
  <div class="abs back__photo" role="img" aria-label="Foto: Überwachungskamera an der Decke, Einbrecher im dunklen Wohnraum" style="background:linear-gradient(100deg,#c9c3b8 0%,#5e6a78 35%,#1d2a38 60%,#2c3e4f 100%)"></div>
  <div class="abs back__red-lower"></div>
  <div class="abs back__dark-strip"></div>
  <div class="abs back__panel"></div>
  <svg class="abs back__tab" viewBox="0 0 330 36"><polygon points="0,0 330,0 324,36 0,36" fill="#e31e24"/></svg>
  <div class="abs back__tab-text">Warum Sie investieren sollten:</div>

  <div class="abs back__logo">
    <div class="brand"><span class="brand__dot" style="width:14px;height:14px"></span><span class="brand__name" style="font-size:16px">WACHTPUNKT</span></div>
  </div>

  <svg class="benefit__icon" style="top:214px" width="72" height="72" viewBox="0 0 72 72"><circle cx="36" cy="36" r="34" fill="#fff" stroke="#e31e24" stroke-width="2.5"/><circle cx="36" cy="36" r="29" fill="#5a5a5a"/><path d="M22 36l14-12 14 12M26 33v14h20V33" fill="none" stroke="#fff" stroke-width="2.2" stroke-linejoin="round"/><path d="M31 44h10M33 44v-4a3 3 0 0 1 6 0v4" fill="none" stroke="#fff" stroke-width="2"/></svg>
  <div class="benefit__title" style="top:212px">Einbruchschutz:</div>
  <p class="benefit__text" style="top:233px">Jährlich werden tausende Haushalte Opfer von Einbrüchen. Ein professionelles Sicherheitssystem senkt das Risiko drastisch.</p>
  <div class="back__rule" style="top:291px"></div>

  <svg class="benefit__icon" style="top:295px" width="72" height="72" viewBox="0 0 72 72"><circle cx="36" cy="36" r="34" fill="#fff" stroke="#e31e24" stroke-width="2.5"/><circle cx="36" cy="36" r="29" fill="#5a5a5a"/><path d="M22 31l24-8 3 8-24 8z M38 35l2 6h6M46 38v8" fill="none" stroke="#fff" stroke-width="2.2" stroke-linejoin="round"/></svg>
  <div class="benefit__title" style="top:305px">Überwachung:</div>
  <p class="benefit__text" style="top:326px">Modernste Kamerasysteme bieten Ihnen ein Auge vor Ort – auch, wenn Sie unterwegs sind.</p>
  <div class="back__rule" style="top:372px"></div>

  <svg class="benefit__icon" style="top:375px;left:44px" width="72" height="72" viewBox="0 0 72 72"><circle cx="36" cy="36" r="34" fill="#fff" stroke="#e31e24" stroke-width="2.5"/><circle cx="36" cy="36" r="29" fill="#5a5a5a"/><path d="M27 20h18v5H27z" fill="none" stroke="#fff" stroke-width="2"/><path d="M36 33c5 6 7 9 7 13a7 7 0 0 1-14 0c0-4 3-6 4-9 1 2 2 3 3 3z" fill="none" stroke="#fff" stroke-width="2" stroke-linejoin="round"/></svg>
  <div class="benefit__title" style="top:389px">Frühzeitige Brandmeldung:</div>
  <p class="benefit__text" style="top:410px">Brände sind unberechenbar. Eine schnelle Warnung schützt Leben und Eigentum.</p>

  <svg class="abs back__portrait" viewBox="0 0 300 201">
    <defs><linearGradient id="gOffice" x1="0" x2="1"><stop offset="0" stop-color="#eef0f2"/><stop offset=".6" stop-color="#c9ced4"/><stop offset="1" stop-color="#1f2a3a"/></linearGradient></defs>
    <polygon points="0,0 272,0 233,201 0,201" fill="url(#gOffice)" role="img" aria-label="Foto: Sicherheitsberater am Telefon im Büro"/>
  </svg>

  <h2 class="abs back__why">Warum Sie<br>investieren sollten:</h2>
  <div class="abs back__why-rule"></div>
  <ul class="abs back__list">
    <li><svg width="11" height="11" viewBox="0 0 12 12"><circle cx="6" cy="6" r="6" fill="#fff"/><path d="M3.3 6.2l1.8 1.8 3.6-3.6" fill="none" stroke="#8f0f14" stroke-width="1.6"/></svg><span>Rund-um-die-Uhr-Sicherheit</span></li>
    <li><svg width="11" height="11" viewBox="0 0 12 12"><circle cx="6" cy="6" r="6" fill="#fff"/><path d="M3.3 6.2l1.8 1.8 3.6-3.6" fill="none" stroke="#8f0f14" stroke-width="1.6"/></svg><span>Einfache Bedienung und<br>modernste Technologie</span></li>
    <li><svg width="11" height="11" viewBox="0 0 12 12"><circle cx="6" cy="6" r="6" fill="#fff"/><path d="M3.3 6.2l1.8 1.8 3.6-3.6" fill="none" stroke="#8f0f14" stroke-width="1.6"/></svg><span>Langfristige Investition in<br>Ihre Lebensqualität</span></li>
  </ul>

  <footer class="abs back__footer">
    <div class="abs contact__role">Ihr Gefahrenexperte:</div>
    <div class="abs contact__name">Jonas Berkel</div>
    <div class="abs contact__line">
      <span><svg width="10" height="10" viewBox="0 0 10 10"><circle cx="5" cy="5" r="5" fill="#fff"/><path d="M3 2.5l1 1-0.6 0.8a4 4 0 0 0 2.3 2.3l0.8-0.6 1 1-0.8 0.9C4.5 7.7 2.3 5.5 2.2 3.3z" fill="#e31e24"/></svg>0151 24680135</span>
      <span><svg width="10" height="10" viewBox="0 0 10 10"><circle cx="5" cy="5" r="5" fill="#fff"/><rect x="2.5" y="3.2" width="5" height="3.6" fill="none" stroke="#e31e24" stroke-width=".9"/><path d="M2.5 3.2L5 5.2 7.5 3.2" fill="none" stroke="#e31e24" stroke-width=".9"/></svg>berkel@wachtpunkt.de</span>
    </div>
    <div class="abs contact__divider"></div>
    <div class="abs contact__address">
      <svg width="10" height="13" viewBox="0 0 10 13" style="margin-top:2px"><path d="M5 0a4.5 4.5 0 0 0-4.5 4.5C.5 8 5 13 5 13s4.5-5 4.5-8.5A4.5 4.5 0 0 0 5 0z" fill="#fff"/><circle cx="5" cy="4.5" r="1.7" fill="#e31e24"/></svg>
      <div>WACHTPUNKT GmbH<br>Lindenweg 12B<br>04420 Markranstädt</div>
    </div>
  </footer>
</section>

</body>
</html>
```